Indy Film Production Company/Studio

We need a business card designed from an existing logo. We are a digital studio/production company that caters to creating genre entertainment, like Action, Horror, and martial arts. The card along with the logo will be used to Brand the company from letter heads to banners. The design will also be used for postcards and Brochures. It should be professional and masculine.
Updates

Thank you to all the designers who have participated. I'm narrowing down who it will be. Thank you again.

Target Market(s)

Investors, Networks, Producers, and actors

Industry/Entity Type

Film Production

Contact Information for Business Card

Benedict Harlowe
Producer/Writer/Director
www.pelvarmotionworks.com

Requirements
Must have
• Website address, Facebook icon and Twitter icon possibly in the back of the card.
Nice to have
• Logline of Company: Follow The Action.

```html
<!DOCTYPE html>
<html lang="en">
<head>
<meta charset="utf-8">
<title>Pelvar Motion Works – Business Card</title>
<link href="https://fonts.googleapis.com/css2?family=PT+Sans:wght@400;700&display=swap" rel="stylesheet">
<style>
  :root {
    --backdrop: #d9d6d2;
    --card-black: #141414;
    --card-edge: #0a0a0a;
    --brand-red: #e3232b;
    --text-white: #f2f2f2;
    --text-grey: #b9b9b9;
    --photo-dark: #1c1c1c;
    --photo-mid: #6a6a6a;
  }
  * { margin: 0; padding: 0; box-sizing: border-box; }
  html, body {
    width: 1200px; height: 814px; overflow: hidden;
    background: var(--backdrop);
    font-family: "PT Sans", Arial, sans-serif;
  }
  .stage {
    position: relative; width: 1200px; height: 814px;
    display: flex; align-items: center; justify-content: center; gap: 48px;
  }
  .card {
    position: relative; width: 540px; height: 309px;
    background: var(--card-black);
    box-shadow: 0 6px 18px rgba(0,0,0,.25);
    overflow: hidden;
  }

  /* Front */
  .card-front__photo {
    position: absolute; right: 0; top: 0; width: 300px; height: 100%;
    background: radial-gradient(ellipse at 55% 45%, var(--photo-mid) 0%, #3a3a3a 35%, var(--photo-dark) 70%, var(--card-black) 100%);
  }
  .card-front__info {
    position: absolute; left: 34px; top: 40px; width: 250px;
  }
  .brand-name {
    color: var(--brand-red);
    font-weight: 700; font-size: 25px; line-height: 1.1;
    text-transform: uppercase; letter-spacing: .5px;
  }
  .dotted-rule {
    border-top: 2px dotted var(--brand-red);
    width: 210px; margin: 12px 0 10px;
  }
  .person-name { color: var(--brand-red); font-size: 19px; font-weight: 400; }
  .person-role { color: var(--text-white); font-size: 15px; margin-top: 2px; }
  .contact-list { list-style: none; margin-top: 4px; }
  .contact-item {
    display: flex; align-items: center; gap: 12px;
    color: var(--text-white); font-size: 15px; line-height: 24px;
  }
  .contact-icon { width: 13px; height: 13px; flex: none; }

  /* Back */
  .card-back { display: flex; flex-direction: column; align-items: center; justify-content: center; }
  .card-back__social {
    position: absolute; top: 12px; right: 14px; width: 14px; height: 14px;
    background: #3a3a3a;
  }
  .card-back__brand {
    color: var(--text-grey); font-weight: 700; font-size: 34px;
    text-transform: uppercase; letter-spacing: 1px;
  }
  .card-back__web {
    color: var(--text-grey); font-size: 12px; letter-spacing: 5px; margin-top: 18px;
  }
</style>
</head>
<body>
<main class="stage">
  <section class="card card-front">
    <div class="card-front__photo" role="img" aria-label="Photograph of a cinema camera rig on a tripod head"></div>
    <div class="card-front__info">
      <div class="brand-name">Pelvar Motion Works</div>
      <div class="dotted-rule"></div>
      <div class="person-name">Benedict Harlowe</div>
      <div class="person-role">Producer/Writer/Director</div>
      <div class="dotted-rule"></div>
      <ul class="contact-list">
        <li class="contact-item">
          <svg class="contact-icon" viewBox="0 0 16 16"><path fill="var(--brand-red)" d="M3 1l3 3-1.5 2c1 2 3.5 4.5 5.5 5.5L12 10l3 3-2 2C7 15 1 9 1 3z"/></svg>
          555 014 2290
        </li>
        <li class="contact-item">
          <svg class="contact-icon" viewBox="0 0 16 16"><rect x="1" y="3" width="14" height="10" fill="var(--brand-red)"/><path d="M1 3l7 6 7-6" fill="none" stroke="var(--card-black)" stroke-width="1.5"/></svg>
          hello@pelvarmotion.com
        </li>
        <li class="contact-item">
          <svg class="contact-icon" viewBox="0 0 16 16"><circle cx="8" cy="8" r="7" fill="var(--brand-red)"/><path d="M1 8h14M8 1c-3 4-3 10 0 14M8 1c3 4 3 10 0 14" fill="none" stroke="var(--card-black)" stroke-width="1.2"/></svg>
          www.pelvarmotionworks.com
        </li>
      </ul>
    </div>
  </section>

  <section class="card card-back">
    <div class="card-back__social"></div>
    <div class="card-back__brand">Pelvar Motion Works</div>
    <div class="card-back__web">www.pelvarmotionworks.com</div>
  </section>
</main>
</body>
</html>
```